"Thank You" card for professional property management agency.

We need to create a DL size "Thank You" card primarily used to thank new clients for their business and referrals.
We are a real estate agency based on Sydney's Northern Beaches. We want the card to feel happy and professional, incorporating our logo.
See our website for details about our business - www.harbourleafrealty.com.au
We have attached our logo in black text and white text as well as some images we have used across our website.
One side must have the ability to hand write a message of thank you on.
I would like this to be a clean and simple design, feel free to use any image supplied, but we are also happy with plain or patterned designs too.

Target Market(s)

Property investors male and female aged 30-60

Industry/Entity Type

Real Estate

Font styles to use
Other font styles liked:
• Please let the designer choose font

Colors

Designer to choose colors to be used in the design.

Requirements
Must have
• DL Size: Full Bleed 213x102mm. Doc size 210x99mm (horizontal)
• Harbour Leaf Realty Logo
• Contact Details:
• info@harbourleafrealty.com.au
• Tel: 0498 217 603
• Level 2, 17 Wattlecombe Rd, Wattlecombe NSW 2187
• "Thank You" somewhere on the card
• Area or side to write message on.
• Design to be provided in editable photoshop PSD file and print ready PDF file
Nice to have
• Sleek professional design that feels "happy or grateful" as it is a thank you card
• Happy to use a plain colour or pattern on one side - it does not have to be an image provided, but feel free to design with either.
Should not have
• should not be too busy, keep it clean and simple.

```html
<!DOCTYPE html>
<html lang="en">
<head>
<meta charset="utf-8">
<title>Harbour Leaf Realty – Thank You Card</title>
<link href="https://fonts.googleapis.com/css2?family=Montserrat:wght@700&family=Lato:wght@400&family=Parisienne&display=swap" rel="stylesheet">
<style>
  :root {
    --stage: #ece8e4;
    --paper: #ffffff;
    --gold: #c9a24a;
    --gold-soft: #e8d29c;
    --ink: #1d1d1f;
    --teal: #2f7f86;
    --rule: #b9b9b9;
  }
  * { box-sizing: border-box; margin: 0; padding: 0; }
  html, body { width: 1200px; height: 675px; overflow: hidden; }
  body {
    background: var(--stage);
    display: flex;
    align-items: center;
    justify-content: center;
    gap: 36px;
    font-family: "Lato", sans-serif;
    color: var(--ink);
  }
  .card {
    position: relative;
    width: 560px;
    height: 264px;
    background: var(--paper);
    box-shadow: 0 2px 10px rgba(0,0,0,0.12);
    overflow: hidden;
  }
  .card__pattern {
    position: absolute;
    inset: 0;
    background: linear-gradient(135deg, #fbf6ea 0%, var(--gold-soft) 45%, #fdf9f0 70%, #e2c788 100%);
  }
  .panel {
    position: absolute;
    background: var(--paper);
    box-shadow: 0 1px 4px rgba(0,0,0,0.15);
  }
  .panel::after {
    content: "";
    position: absolute;
    inset: 7px;
    border: 1.5px solid var(--gold);
    pointer-events: none;
  }

  /* Front */
  .panel--contact {
    right: 34px;
    top: 44px;
    width: 300px;
    height: 176px;
    padding: 24px 26px 20px;
    display: flex;
    flex-direction: column;
    align-items: flex-end;
  }
  .brand {
    display: flex;
    align-items: center;
    gap: 8px;
    font-family: "Montserrat", sans-serif;
    font-weight: 700;
    color: var(--ink);
    text-transform: uppercase;
    white-space: nowrap;
  }
  .brand__dot {
    width: 14px; height: 14px; border-radius: 50%;
    background: var(--teal);
    flex: none;
  }
  .brand--large { font-size: 19px; letter-spacing: 0.5px; align-self: center; margin-bottom: 20px; }
  .brand--small { font-size: 10px; letter-spacing: 0.3px; gap: 5px; }
  .brand--small .brand__dot { width: 8px; height: 8px; }
  .contact { text-align: right; font-size: 11.5px; line-height: 1.45; }
  .contact__email { margin-top: 10px; }

  /* Back */
  .panel--message {
    inset: 16px 18px;
    padding: 34px 40px 26px;
  }
  .rules { list-style: none; }
  .rules li {
    height: 26px;
    border-bottom: 1px dashed var(--rule);
  }
  .message-foot {
    position: absolute;
    left: 40px; right: 40px; bottom: 24px;
    display: flex;
    align-items: flex-end;
    justify-content: space-between;
  }
  .thanks {
    font-family: "Parisienne", cursive;
    font-size: 30px;
    color: var(--gold);
    line-height: 1;
  }
</style>
</head>
<body>

  <section class="card card--front" aria-label="Card front">
    <div class="card__pattern" role="img" aria-label="Gold geometric line pattern on white"></div>
    <div class="panel panel--contact">
      <div class="brand brand--large"><span class="brand__dot"></span>Harbour Leaf Realty</div>
      <address class="contact" style="font-style:normal">
        <p>Level 2, 17 Wattlecombe Rd</p>
        <p>Wattlecombe NSW 2187</p>
        <p>Tel: 0498 217 603</p>
        <p class="contact__email">info@harbourleafrealty.com.au</p>
      </address>
    </div>
  </section>

  <section class="card card--back" aria-label="Card back">
    <div class="card__pattern" role="img" aria-label="Gold geometric line pattern on white"></div>
    <div class="panel panel--message">
      <ul class="rules">
        <li></li><li></li><li></li><li></li><li></li>
      </ul>
      <div class="message-foot">
        <div class="brand brand--small"><span class="brand__dot"></span>Harbour Leaf Realty</div>
        <p class="thanks">Thank You</p>
      </div>
    </div>
  </section>

</body>
</html>
```